Fancy looking Inspection Postcard

Postcard needed for customers to inspect their product once it is delivered. We'll be giving them the steps for inspecting their product and to contact us if any issues arise. Would like to see something that sticks out but uses our company's colors. Would like to see creativity. Possibly utilizing the diamond steel background like we have in our logo.

Target Market(s)

Customers of our manufacturing shop

Industry/Entity Type

Manufacturing - metal wall art, custom products

Requirements
Must have
• our colors and logo
Nice to have
• get creative. i like creativity

```html
<!DOCTYPE html>
<html lang="en">
<head>
<meta charset="utf-8">
<title>Product Inspection Postcard</title>
<link rel="stylesheet" href="https://fonts.googleapis.com/css2?family=Barlow+Condensed:wght@600;700&family=Archivo:wght@800&family=Inter:wght@300;400&display=swap">
<style>
  :root {
    --page: #e8e8e8;
    --plate-dark: #1d1d1d;
    --plate-mid: #333333;
    --green: #76a643;
    --yellow: #fff200;
    --ink: #111111;
    --white: #ffffff;
    --rule: #8a8a8a;
  }
  * { margin: 0; padding: 0; box-sizing: border-box; }
  html, body { width: 965px; height: 1200px; overflow: hidden; background: var(--page); }
  .postcard {
    position: absolute; left: 32px; top: 300px; width: 900px; height: 600px;
    box-shadow: 0 18px 30px rgba(0,0,0,.18); overflow: hidden;
  }
  .plate-texture {
    position: absolute; inset: 0;
    background: radial-gradient(circle at 40% 40%, var(--plate-mid), var(--plate-dark) 75%);
  }
  .steps { position: absolute; left: 35px; top: 35px; display: flex; gap: 13px; }
  .step {
    width: 198px; height: 351px; border-radius: 8px; padding: 26px 19px 0 19px;
  }
  .step--green { background: var(--green); color: var(--white); }
  .step--yellow { background: var(--yellow); color: var(--ink); }
  .step__number {
    font-family: "Barlow Condensed", sans-serif; font-weight: 700; font-size: 30px;
    line-height: 1; letter-spacing: -0.5px;
  }
  .step__title {
    font-family: "Archivo", sans-serif; font-weight: 800; font-size: 20px;
    line-height: 1.2; letter-spacing: -0.8px; margin-top: 8px; height: 58px;
  }
  .step__icon { display: block; width: 72px; height: 72px; margin-top: 8px; }
  .step__questions {
    font-family: "Inter", sans-serif; font-weight: 300; font-size: 19px;
    line-height: 1.2; letter-spacing: -1px; margin-top: 22px;
  }
  .step__questions p + p { margin-top: 5px; }
  .review { position: absolute; left: 35px; top: 436px; width: 270px; }
  .review__title {
    font-family: "Barlow Condensed", sans-serif; font-weight: 700; font-size: 36px;
    color: var(--green); letter-spacing: -0.8px; line-height: 1;
  }
  .review__text {
    font-family: "Inter", sans-serif; font-weight: 300; font-size: 18px;
    color: var(--white); line-height: 1.35; letter-spacing: -1px; margin-top: 10px;
  }
  .divider { position: absolute; left: 318px; top: 448px; width: 1px; height: 108px; background: var(--rule); }
  .contact { position: absolute; left: 352px; top: 436px; color: var(--white);
    font-family: "Inter", sans-serif; font-weight: 300; font-size: 19px; line-height: 23px; letter-spacing: -0.6px; }
  .contact__row { display: flex; gap: 20px; margin-bottom: 6px; }
  .contact__row svg { width: 16px; height: 16px; margin-top: 4px; flex: none; }
  .brand {
    position: absolute; left: 735px; top: 440px; width: 130px; text-align: center;
  }
  .brand__dot { width: 44px; height: 44px; border-radius: 50%; background: var(--green); margin: 0 auto 10px; }
  .brand__name {
    font-family: "Archivo", sans-serif; font-weight: 800; font-size: 20px;
    color: var(--yellow); line-height: 1.1; letter-spacing: -0.5px;
  }
</style>
</head>
<body>
<main class="postcard">
  <div class="plate-texture" role="img" aria-label="Dark diamond steel plate texture"></div>

  <section class="steps">
    <article class="step step--green">
      <div class="step__number">Step 1</div>
      <h2 class="step__title">Inspect General Shapes</h2>
      <svg class="step__icon" viewBox="0 0 72 72" fill="none" stroke="currentColor" stroke-width="2">
        <rect x="2" y="42" width="26" height="26"/>
        <circle cx="34" cy="38" r="16"/>
        <path d="M56 2 L72 36 L40 36 Z"/>
      </svg>
      <div class="step__questions">
        <p>Is it what you expected?</p>
        <p>Is it bent, disoriented?</p>
      </div>
    </article>

    <article class="step step--yellow">
      <div class="step__number">Step 2</div>
      <h2 class="step__title">Inspect The Welds, If Any</h2>
      <svg class="step__icon" viewBox="0 0 72 72" fill="none" stroke="currentColor" stroke-width="2">
        <rect x="8" y="4" width="32" height="50" rx="2"/>
        <rect x="13" y="10" width="22" height="16"/>
        <path d="M2 66 H70 M10 60 H60 M40 50 L62 44 L66 54 L44 58 Z M30 40 L38 34 M32 46 L42 40"/>
      </svg>
      <div class="step__questions">
        <p>Do they look<br>clean?</p>
        <p>Are there any<br>gaps?</p>
      </div>
    </article>

    <article class="step step--green">
      <div class="step__number">Step 3</div>
      <h2 class="step__title">Inspect The Finish</h2>
      <svg class="step__icon" viewBox="0 0 72 72" fill="none" stroke="currentColor" stroke-width="2">
        <rect x="2" y="8" width="62" height="62"/>
        <circle cx="33" cy="39" r="18"/>
        <circle cx="33" cy="39" r="8"/>
        <path d="M33 14 V64 M8 39 H58 M50 20 L66 2"/>
      </svg>
      <div class="step__questions">
        <p>Are there any areas not finished?</p>
        <p>Are the colors what you expected?</p>
      </div>
    </article>

    <article class="step step--yellow">
      <div class="step__number">Step 4</div>
      <h2 class="step__title">Check For Functionality</h2>
      <svg class="step__icon" viewBox="0 0 72 72" fill="none" stroke="currentColor" stroke-width="2.5">
        <circle cx="44" cy="28" r="20" stroke-dasharray="8 4"/>
        <circle cx="26" cy="30" r="20"/>
        <circle cx="26" cy="30" r="13"/>
        <path d="M40 44 L64 66"/>
      </svg>
      <div class="step__questions">
        <p>Does it work the way you want it to?</p>
        <p>Is it what you expected?</p>
      </div>
    </article>
  </section>

  <section class="review">
    <h1 class="review__title">Did we do a god job?</h1>
    <p class="review__text">If you think so, leave us a review on Reviewly? If not let us know?</p>
  </section>

  <div class="divider"></div>

  <section class="contact">
    <div class="contact__row">
      <svg viewBox="0 0 16 16"><circle cx="8" cy="8" r="7" fill="#76a643"/><path d="M3 6 Q8 8 13 5 M8 1 Q5 8 8 15" stroke="#1d1d1d" stroke-width="1.3" fill="none"/></svg>
      <div>ridgeworksfab.com/contact</div>
    </div>
    <div class="contact__row">
      <svg viewBox="0 0 16 16"><rect x="1" y="3" width="14" height="10" fill="#76a643"/><path d="M1 3 L8 9 L15 3" stroke="#1d1d1d" stroke-width="1.3" fill="none"/></svg>
      <div>info@ridgeworksfab.com<br>orders@ridgeworksfab.com</div>
    </div>
    <div class="contact__row">
      <svg viewBox="0 0 16 16"><path d="M3 1 L6 1 L7 5 L5 6 Q6 9 10 11 L11 9 L15 10 L15 13 Q14 15 11 15 Q2 12 1 4 Q1 2 3 1 Z" fill="#76a643"/></svg>
      <div>555 010 2244<br>555 010 7781</div>
    </div>
  </section>

  <div class="brand">
    <div class="brand__dot"></div>
    <div class="brand__name">Copper Ridge Works</div>
  </div>
</main>
</body>
</html>
```